Hadley & Partners, LLC Business Card 2016

We need a new business card design for a very important trade show coming up.

We are a compliance Consulting Firm. Our clients are stock brokerage firms and investment advisers.

I would like our logo on both sides of the card.

Info in the front of the card shold include:

Logo
First & Last Name
Title
Office #
Cell #
Email
Company Address (42 W. Calloway St., Suite 300 Pasadena, CA 91417

Back of the card should include the logo and url: www.hadleypartnersgroup.com

Target Market(s)

Stock Brokerage Firms and Investment Advisers

Industry/Entity Type

Financial Service

Contact Information for Business Card

Marcus J. Pellew
President
42 W. Calloway St., Suite 300
Pasadena, CA 91417
O 626.555.0147 ext. 204
C 818.555.0193
Email: marcus@hadleypartnersgroup.com
www.hadleypartnersgroup.com

Requirements
Nice to have
• The back of the card could be black with the logo with the white letters.
• I do want the front of the card to at least have the color logo with the black "Hadley & Partners Lettering.

```html
<!DOCTYPE html>
<html lang="en">
<head>
<meta charset="utf-8">
<title>Hadley &amp; Partners — Business Card</title>
<link rel="stylesheet" href="https://fonts.googleapis.com/css2?family=Source+Sans+3:wght@400;600&display=swap">
<style>
  :root {
    --backdrop: #3b2c33;
    --card-dark: #231f20;
    --card-light: #ffffff;
    --ink: #231f20;
    --ink-soft: #2b2b2b;
    --paper-text: #ffffff;
    --accent: #e0242a;
    --font-text: "Source Sans 3", "Myriad Pro", Arial, sans-serif;
  }
  * { box-sizing: border-box; margin: 0; padding: 0; }
  html, body {
    width: 1200px; height: 1200px; overflow: hidden;
    background: var(--backdrop);
    font-family: var(--font-text);
  }
  .canvas { position: relative; width: 1200px; height: 1200px; }

  .card {
    position: absolute; left: 208px; width: 784px; height: 446px;
    border-radius: 20px;
    box-shadow: 0 6px 14px rgba(0,0,0,0.35);
  }
  .card--back { top: 120px; background: var(--card-dark); }
  .card--front { top: 636px; background: var(--card-light); }

  /* brand lockup: plain square + name */
  .brand { position: absolute; display: flex; align-items: center; gap: 16px; }
  .brand__square { background: var(--accent); flex: none; }
  .brand__name { font-weight: 600; letter-spacing: 0.04em; text-transform: uppercase; white-space: nowrap; }

  .card--back .brand { left: 0; right: 0; top: 186px; justify-content: center; }
  .card--back .brand__name { color: var(--paper-text); font-size: 46px; }
  .card--back .brand__square { width: 56px; height: 56px; }

  .back__url {
    position: absolute; left: 0; right: 0; top: 394px;
    text-align: center; color: var(--paper-text); font-size: 20px; font-weight: 400;
  }

  .card--front .brand {
    left: 20px; width: 300px; top: 150px;
    flex-direction: column; gap: 18px;
  }
  .card--front .brand__name { color: var(--ink); font-size: 24px; }
  .card--front .brand__square { width: 64px; height: 64px; }

  .divider {
    position: absolute; left: 341px; top: 68px; width: 2px; height: 306px;
    background: linear-gradient(to bottom, rgba(224,36,42,0), var(--accent) 15%, var(--accent) 85%, rgba(224,36,42,0));
  }

  .contact { position: absolute; left: 378px; top: 106px; color: var(--ink-soft); }
  .contact__name { font-size: 31px; font-weight: 400; line-height: 1.1; color: var(--ink); }
  .contact__title { font-size: 21px; color: var(--accent); line-height: 1.2; }
  .contact__address { margin-top: 22px; font-size: 21px; line-height: 26px; }
  .contact__list { list-style: none; margin-top: 20px; font-size: 21px; line-height: 26.5px; }
  .contact__list li { display: flex; align-items: center; }
  .contact__icon { width: 18px; height: 18px; margin-right: 12px; flex: none; fill: var(--accent); }
</style>
</head>
<body>
<main class="canvas">

  <section class="card card--back" aria-label="Card back">
    <div class="brand">
      <span class="brand__square"></span>
      <span class="brand__name">Hadley &amp; Partners</span>
    </div>
    <p class="back__url">www.hadleypartnersgroup.com</p>
  </section>

  <section class="card card--front" aria-label="Card front">
    <div class="brand">
      <span class="brand__square"></span>
      <span class="brand__name">Hadley &amp; Partners</span>
    </div>

    <div class="divider"></div>

    <div class="contact">
      <h1 class="contact__name">Marcus J. Pellew</h1>
      <p class="contact__title">President</p>
      <p class="contact__address">42 W. Calloway St., Suite 300<br>Pasadena, CA 91417</p>
      <ul class="contact__list">
        <li>
          <svg class="contact__icon" viewBox="0 0 20 20" aria-hidden="true">
            <path d="M1 7c0-3 4-5 9-5s9 2 9 5v2h-5V6.5c-1-.5-2.5-.7-4-.7s-3 .2-4 .7V9H1z"/>
            <path d="M4 10l3-3h6l3 3v8H4z"/>
            <circle cx="10" cy="13" r="2.2" fill="#fff"/>
          </svg>626.555.0147 ext. 204
        </li>
        <li>
          <svg class="contact__icon" viewBox="0 0 20 20" aria-hidden="true">
            <path d="M5 1h10a1.5 1.5 0 0 1 1.5 1.5v15A1.5 1.5 0 0 1 15 19H5a1.5 1.5 0 0 1-1.5-1.5v-15A1.5 1.5 0 0 1 5 1zm.5 2.5v11h9v-11z"/>
          </svg>818.555.0193
        </li>
        <li>
          <svg class="contact__icon" viewBox="0 0 20 20" aria-hidden="true">
            <path d="M1 4h18v12H1zm2 2v.4l7 5 7-5V6l-7 5zm0 3v5h3.5zm14 0l-3.5 5H17z"/>
          </svg>marcus@hadleypartnersgroup.com
        </li>
        <li>
          <svg class="contact__icon" viewBox="0 0 20 20" aria-hidden="true" fill="none" stroke="#e0242a" stroke-width="1.5" style="fill:none">
            <circle cx="10" cy="10" r="8.2"/>
            <ellipse cx="10" cy="10" rx="3.6" ry="8.2"/>
            <path d="M2 7.5h16M2 12.5h16M10 1.8v16.4"/>
          </svg>www.hadleypartnersgroup.com
        </li>
      </ul>
    </div>
  </section>

</main>
</body>
</html>
```